1/4 page magazine ad

We would like a 1/4 ad in a magazine advertising a doctor in our practice. Dr. Clara Mendt, DC is the only Female Brinley Certified chiropractor in Williamsburg, VA. We would like the ad to include a large eye catching picture of a woman's pregnant belly, as the Brinley technique is for pregnant women. Please take a look at our previous ad that we have had done to see some of the elements that we liked in our other ad.

```html
<!DOCTYPE html>
<html lang="en">
<head>
<meta charset="utf-8">
<title>Dr. Clara Mendt, DC – Quarter Page Ad</title>
<link rel="stylesheet" href="https://fonts.googleapis.com/css2?family=Bebas+Neue&display=swap">
<style>
  :root {
    --page-bg: #ececec;
    --brand-red: #b81c3c;
    --ink: #111111;
    --white: #ffffff;
    --sky-blue: #2f6fc2;
    --violet: #6a4fb8;
    --pale-blue: #dfe6f3;
  }
  * { margin: 0; padding: 0; box-sizing: border-box; }
  html, body {
    width: 1200px; height: 1200px; overflow: hidden;
    background: var(--page-bg);
    font-family: "Bebas Neue", "Arial Narrow", sans-serif;
  }
  .ad {
    position: absolute; left: 200px; top: 85px;
    width: 798px; height: 1030px; overflow: hidden;
    background: var(--white);
    box-shadow: 0 2px 6px rgba(0,0,0,0.18);
  }
  .ad-shapes { position: absolute; inset: 0; width: 100%; height: 100%; }
  .phone {
    position: absolute; left: 52px; top: 74px;
    display: flex; align-items: center; gap: 14px;
    color: var(--white); font-size: 54px; letter-spacing: 1px; line-height: 1;
  }
  .phone svg { width: 36px; height: 36px; }
  .practice-name {
    position: absolute; left: 452px; top: 64px; width: 296px;
    display: flex; align-items: center; gap: 10px;
    color: var(--brand-red); font-size: 32px; line-height: 0.95; letter-spacing: 1px;
  }
  .practice-name .mark { width: 22px; height: 22px; background: var(--brand-red); flex: none; }
  .headline {
    position: absolute; left: 88px; top: 318px;
    color: var(--white); font-size: 104px; line-height: 0.98; font-weight: 400;
    text-shadow: 6px 4px 0 var(--ink);
  }
  .doctor-photo {
    position: absolute; left: 109px; top: 580px; width: 144px; height: 217px;
    background: linear-gradient(180deg, #6d7a45 0%, #5a4636 55%, #1d2740 100%);
  }
  .doctor-name {
    position: absolute; left: 56px; top: 834px;
    color: var(--ink); font-size: 38px; letter-spacing: 0.5px;
  }
  .credential {
    position: absolute; left: 56px; top: 922px;
    color: var(--ink); font-size: 23px; line-height: 1.4; letter-spacing: 0.3px;
  }
</style>
</head>
<body>
<div class="ad">
  <svg class="ad-shapes" viewBox="0 0 798 1030" preserveAspectRatio="none">
    <defs>
      <linearGradient id="spineBlue" x1="0" y1="0" x2="1" y2="1">
        <stop offset="0" stop-color="#9ec3ef"/>
        <stop offset="0.4" stop-color="#2f6fc2"/>
        <stop offset="0.7" stop-color="#6a4fb8"/>
        <stop offset="1" stop-color="#c96a8a"/>
      </linearGradient>
      <radialGradient id="featureRed" cx="0.55" cy="0.5" r="0.65">
        <stop offset="0" stop-color="#f2a0a8"/>
        <stop offset="0.35" stop-color="#d63a55"/>
        <stop offset="0.75" stop-color="#9a1430"/>
        <stop offset="1" stop-color="#3a0a1e"/>
      </radialGradient>
      <linearGradient id="paleSweep" x1="0" y1="0" x2="1" y2="0">
        <stop offset="0" stop-color="#ffffff"/>
        <stop offset="1" stop-color="#dfe6f3"/>
      </linearGradient>
    </defs>
    <rect class="backdrop-illustration" width="798" height="1030" fill="url(#spineBlue)" role="img" aria-label="Soft glowing blue medical illustration background"/>
    <path class="top-swoosh" d="M0,0 L355,0 C380,120 520,168 560,175 C330,178 70,240 0,440 Z" fill="var(--white)"/>
    <path class="top-band" d="M0,0 L340,0 C360,110 480,160 530,168 C310,175 60,230 0,420 Z" fill="var(--brand-red)"/>
    <path class="bottom-sweep" d="M0,720 C160,600 520,590 798,660 L798,1030 L0,1030 Z" fill="url(#paleSweep)"/>
    <circle class="feature-photo" cx="805" cy="795" r="455" fill="url(#featureRed)" role="img" aria-label="Large photo of a pregnant woman's belly"/>
  </svg>

  <div class="phone">
    <svg viewBox="0 0 24 24" fill="none" stroke="currentColor" stroke-width="2.2" stroke-linecap="round" stroke-linejoin="round" aria-hidden="true">
      <path d="M5 3h4l2 5-2.5 1.5a11 11 0 0 0 6 6L16 13l5 2v4a2 2 0 0 1-2 2A17 17 0 0 1 3 5a2 2 0 0 1 2-2z"/>
      <path d="M15 3a6 6 0 0 1 6 6"/>
    </svg>
    <span>757.555.0148</span>
  </div>

  <div class="practice-name"><span class="mark"></span><span>Harborline Spine Center</span></div>

  <h1 class="headline">Neck or<br>Back Pain?</h1>

  <div class="doctor-photo" role="img" aria-label="Portrait photo of Dr. Clara Mendt"></div>
  <p class="doctor-name">Dr. Clara Mendt, DC</p>
  <p class="credential">Female Brinley Certified<br>Chiropractor in Williamsburg, VA</p>
</div>
</body>
</html>
```